Education Certificate

We need a modern yet professional Certificate for those who successfully pass / complete our online Training course.

There are various courses but ONE certificate design required.

the certificate needs to look extremely professional and of value.

```html
<!DOCTYPE html>
<html lang="en">
<head>
<meta charset="UTF-8">
<title>Certificate of Completion</title>
<link rel="stylesheet" href="https://fonts.googleapis.com/css2?family=Poppins:wght@400;500;700&family=Allura&family=Cinzel:wght@600&display=swap">
<style>
  :root {
    --page-bg: #d9dae4;
    --navy: #1d2c6c;
    --navy-deep: #18255c;
    --yellow: #f3d80c;
    --gold: #c9a23a;
    --gold-light: #e9c85a;
    --paper: #f8f8f9;
    --ink: #1b1b22;
  }
  html, body {
    margin: 0;
    padding: 0;
    width: 834px;
    height: 1200px;
    overflow: hidden;
    background: var(--page-bg);
  }
  .certificate {
    position: absolute;
    left: 67px;
    top: 330px;
    width: 700px;
    height: 540px;
    background: linear-gradient(160deg, #ffffff 0%, var(--paper) 55%, #efeff2 100%);
    box-shadow: 0 4px 14px rgba(30, 35, 70, 0.18);
    overflow: hidden;
    font-family: 'Poppins', sans-serif;
  }
  .header-band {
    position: absolute;
    left: 0; top: 0;
    width: 700px;
    height: 220px;
    background: linear-gradient(135deg, var(--navy) 0%, var(--navy-deep) 100%);
  }
  .gold-frame {
    position: absolute;
    left: 28px; top: 28px;
    width: 642px; height: 484px;
    box-sizing: border-box;
    border: 1.5px solid var(--gold);
  }
  .institute {
    position: absolute;
    left: 295px; top: 55px;
    width: 117px; height: 45px;
    box-sizing: border-box;
    border: 1px solid #0e153a;
    display: flex;
    align-items: center;
  }
  .institute-square {
    width: 40px; height: 43px;
    background: #ffffff;
    flex: none;
  }
  .institute-name {
    margin-left: 6px;
    color: #ffffff;
    font-size: 7.6px;
    line-height: 9px;
    font-weight: 400;
    letter-spacing: 0.1px;
  }
  .centered {
    position: absolute;
    left: 0; right: 0;
    text-align: center;
    line-height: 1;
    margin: 0;
  }
  .title {
    top: 121px;
    color: var(--yellow);
    font-size: 49px;
    font-weight: 700;
    letter-spacing: 0.5px;
  }
  .subtitle {
    top: 174px;
    left: 8px;
    color: #ffffff;
    font-size: 23px;
    font-weight: 400;
    letter-spacing: 4.6px;
  }
  .presented {
    top: 238px;
    color: var(--ink);
    font-size: 16px;
    font-weight: 500;
    letter-spacing: 0.4px;
  }
  .recipient {
    top: 262px;
    left: 12px;
    color: var(--ink);
    font-family: 'Allura', cursive;
    font-size: 72px;
    line-height: 1;
  }
  .rule {
    position: absolute;
    height: 1px;
    background: var(--navy);
  }
  .rule-name { left: 166px; top: 325px; width: 367px; }
  .rule-course { left: 166px; top: 388px; width: 367px; }
  .reason {
    top: 346px;
    color: var(--ink);
    font-size: 14.5px;
    font-weight: 400;
    letter-spacing: 0.3px;
  }
  .rule-signature { left: 93px; top: 449px; width: 147px; }
  .rule-date { left: 454px; top: 449px; width: 147px; }
  .field-label {
    position: absolute;
    top: 461px;
    width: 147px;
    text-align: center;
    font-family: 'Cinzel', serif;
    font-weight: 600;
    font-size: 11.5px;
    letter-spacing: 0.6px;
    color: var(--navy);
    line-height: 1;
  }
  .label-signature { left: 93px; }
  .label-date { left: 454px; }
  .award-seal {
    position: absolute;
    left: 305px; top: 400px;
    width: 90px; height: 90px;
  }
</style>
</head>
<body>
  <main class="certificate">
    <div class="header-band"></div>
    <div class="gold-frame"></div>

    <div class="institute">
      <div class="institute-square"></div>
      <div class="institute-name">GLOBAL CLIENT<br>SERVICE<br>ACADEMY</div>
    </div>

    <h1 class="centered title">CERTIFICATE</h1>
    <p class="centered subtitle">OF COMPLETION</p>

    <p class="centered presented">THIS CERTIFICATE IS PROUDLY PRESENTED TO</p>
    <p class="centered recipient">Clara Hughes</p>
    <div class="rule rule-name"></div>

    <p class="centered reason">For successfully completing our online training course.</p>
    <div class="rule rule-course"></div>

    <svg class="award-seal" viewBox="0 0 90 90" role="img" aria-label="Gold award seal">
      <defs>
        <radialGradient id="sealGold" cx="40%" cy="35%" r="70%">
          <stop offset="0%" stop-color="#f7dd7a"/>
          <stop offset="60%" stop-color="#d9a72e"/>
          <stop offset="100%" stop-color="#b9821c"/>
        </radialGradient>
      </defs>
      <circle cx="45" cy="45" r="42" fill="url(#sealGold)"/>
      <circle cx="45" cy="45" r="32" fill="#1b2a55"/>
    </svg>

    <div class="rule rule-signature"></div>
    <div class="field-label label-signature">SIGNATURE</div>
    <div class="rule rule-date"></div>
    <div class="field-label label-date">DATE</div>
  </main>
</body>
</html>
```